TotHaven Community Landing Page

TotHaven is a virtual world built with childrens' needs in mind. It is an online portal where parents will find all kids' related stuffs and a community connect point for parents to interact and share their experiences.

We need the designs for 2 pages within TotHaven:
- Landing Page for the Community Area
- Registration page for membership

1) The Landing Page need to have the following:

Logo & Main Background :- use the images attached

Page Title & Navigation Menu :-
The page title is "Community Connect"; navigation menu should be able to hold at least 6 tabs

Login Widget* :-
We want to put emphasis on the design of this.
For visitors, this is a normal login widget with username/password input fields, register button and 'login with chatterbook' button.
For logged-in users, this becomes a simple dashboard widget with Avatar, shortlinks and some useful navigation buttons.

"Groups" Section :-
This area holds an image, a short paragraph introducing "Groups", a widget showing 5-10 latest/popular groups and a 'Go to Groups' button at the bottom.

"Forum" Section :-
This area holds an image, a short paragraph introducing "Forum", a widget showing 5-10 latest/popular discussion topics and a 'Go to Forum' button at the bottom.

"Activities" Section -
This area holds an image, a short paragraph introducing "Forum", a widget showing 5-10 latest/popular events & activities and a 'Go to Activities' button at the bottom.

"Marketplace" Section :-
This area holds an image, a short paragraph introducing "Marketplace", a widget showing 5-10 latest/popular products and a 'Go to Marketplace' button at the bottom.

Social Media elements :-
The usual social media icons and chatterbook like box.

2) The Registration Page will need to contain the registration form as per the image attached.

Target Market(s)

Parents with kids ranging from 2 - 12 years old

Industry/Entity Type

Events

Requirements
Nice to have
• - colorful illustrations of kids or kids related images all around

```html
<!DOCTYPE html>
<html lang="en">
<head>
<meta charset="utf-8">
<title>TotHaven – Create Your Account</title>
<link href="https://fonts.googleapis.com/css2?family=Sniglet:wght@400;800&family=Alfa+Slab+One&family=Open+Sans:wght@400;600;700&display=swap" rel="stylesheet">
<style>
  :root {
    --sky-top: #2aa3de;
    --sky-low: #c6e9f7;
    --grass-light: #8dbb3c;
    --grass-dark: #4d7814;
    --hill-green: #8cc424;
    --nav-green: #4aa92c;
    --nav-yellow: #ffe600;
    --nav-text: #2f7d12;
    --brand-blue: #1297d6;
    --panel-light: #def3fb;
    --heading-teal: #3aa6c4;
    --field-text: #3aa6c4;
    --field-border: #bfe3f1;
    --white: #ffffff;
    --submit-top: #8fd13c;
    --submit-bottom: #5ea91f;
    --brand-purple: #9b2fc9;
  }
  * { box-sizing: border-box; margin: 0; padding: 0; }
  html, body { width: 1200px; height: 997px; overflow: hidden; }
  body { position: relative; font-family: "Open Sans", Arial, sans-serif; background: var(--sky-top); }

  .scenery {
    position: absolute; inset: 0;
    background: linear-gradient(180deg, var(--sky-top) 0%, var(--sky-low) 44%, var(--grass-light) 52%, var(--grass-dark) 100%);
  }

  .brand-logo {
    position: absolute; left: 172px; top: 128px; width: 290px;
    display: flex; align-items: center; gap: 10px;
    font-family: "Sniglet", sans-serif; font-weight: 800; font-size: 40px; line-height: 48px; color: var(--brand-purple);
    white-space: nowrap;
  }
  .brand-logo .mark { width: 34px; height: 34px; border-radius: 50%; background: var(--white); flex: none; }

  .title-hill { position: absolute; left: 460px; top: 86px; width: 520px; height: 170px; }
  .page-title {
    position: absolute; left: 495px; top: 126px; width: 320px; text-align: center;
    font-family: "Sniglet", sans-serif; font-weight: 400; font-size: 48px; line-height: 52px; color: #d9f6ff;
    white-space: nowrap;
  }
  .page-title span { display: block; }
  .page-title span + span { padding-left: 26px; color: #f3e6ff; }

  .search {
    position: absolute; left: 917px; top: 142px; width: 246px; height: 43px;
    background: var(--white); border-radius: 10px; padding: 4px;
  }
  .search-field {
    width: 100%; height: 100%; border-radius: 8px; background: #dff3fb;
    font-family: "Sniglet", sans-serif; font-size: 19px; color: var(--brand-blue);
    padding: 6px 10px; position: relative;
  }
  .search-btn { position: absolute; right: 4px; top: 3px; width: 34px; height: 29px; border-radius: 6px; background: var(--brand-blue); }

  .social { position: absolute; left: 972px; top: 201px; display: flex; gap: 6px; }
  .social span { width: 34px; height: 34px; border-radius: 50%; background: var(--brand-blue); border: 2px solid var(--white); }

  .main-nav {
    position: absolute; left: 129px; top: 248px; width: 1047px; height: 50px;
    background: linear-gradient(180deg, #5cc135, var(--nav-green)); border-radius: 6px 6px 0 0;
  }
  .main-nav a {
    position: absolute; top: 6px; height: 36px; border-radius: 6px;
    background: linear-gradient(180deg, #fff46a, var(--nav-yellow) 50%, #f7c900);
    font-family: "Sniglet", sans-serif; font-size: 21px; color: var(--nav-text);
    text-decoration: none; display: flex; align-items: center; justify-content: center;
    box-shadow: 0 2px 3px rgba(0,0,0,.25); white-space: nowrap;
  }

  .content-card {
    position: absolute; left: 142px; top: 296px; width: 1021px; height: 553px;
    background: var(--white); border-radius: 0 0 14px 14px;
  }
  .art { position: absolute; border-radius: 30px; }
  .art-boy-waving { left: 190px; top: 312px; width: 180px; height: 108px; background: radial-gradient(circle, #f6c28a, #e68a2e 70%, transparent 72%); opacity: .75; }
  .art-boy-pencil { left: 893px; top: 305px; width: 205px; height: 130px; background: radial-gradient(circle, #ffd54a, #7cc34a 60%, transparent 72%); opacity: .75; }
  .art-kids-book { left: 740px; top: 604px; width: 284px; height: 230px; background: radial-gradient(ellipse at 50% 45%, #f2a6c0, #f7d66a 45%, #eaf3f7 70%, transparent 74%); }

  .section-heading {
    position: absolute; left: 400px; top: 380px; width: 500px; text-align: center;
    font-family: "Alfa Slab One", serif; font-size: 31px; letter-spacing: 1px; color: var(--heading-teal);
    white-space: nowrap;
  }

  .form-tab {
    position: absolute; left: 207px; top: 403px; width: 176px; height: 34px;
    background: var(--brand-blue); border-radius: 12px 12px 0 0;
    font-family: "Alfa Slab One", serif; font-size: 17px; color: var(--white);
    display: flex; align-items: center; justify-content: center;
  }
  .form-frame {
    position: absolute; left: 150px; top: 434px; width: 1000px; height: 361px;
    background: var(--brand-blue); border-radius: 14px;
  }
  .form-panel {
    position: absolute; left: 166px; top: 452px; width: 967px; height: 327px;
    background: var(--panel-light); border-radius: 12px;
  }
  .field {
    position: absolute; height: 39px; width: 427px;
    background: var(--white); border: 1px solid var(--field-border); border-radius: 10px;
    font-size: 15px; font-weight: 600; color: var(--field-text);
    display: flex; align-items: center; padding-left: 17px;
  }
  .required-mark { position: absolute; font-size: 24px; font-weight: 700; color: var(--field-text); }
  .privacy-note { position: absolute; left: 675px; top: 516px; font-size: 11px; font-weight: 700; color: var(--brand-blue); }
  .required-note {
    position: absolute; left: 760px; top: 549px; width: 245px; text-align: center;
    font-family: "Alfa Slab One", serif; font-size: 18px; line-height: 25px; color: var(--heading-teal);
  }
  .submit-btn {
    position: absolute; left: 191px; top: 700px; width: 163px; height: 60px;
    background: linear-gradient(180deg, var(--submit-top) 0%, #7cc52e 50%, var(--submit-bottom) 52%, var(--submit-bottom) 100%);
    border: 2px solid #b8e37c; border-radius: 10px;
    font-family: "Alfa Slab One", serif; font-size: 25px; color: var(--white);
    display: flex; align-items: center; justify-content: center;
  }

  .footer-logo {
    position: absolute; left: 0; width: 1200px; top: 898px; text-align: center;
    font-family: "Sniglet", sans-serif; font-weight: 800; font-size: 32px; color: #e9f1dc;
  }
  .copyright { position: absolute; left: 0; width: 1200px; top: 957px; text-align: center; font-size: 11px; color: var(--white); }
</style>
</head>
<body>
  <div class="scenery" role="img" aria-label="Sunny sky with rainbow, clouds and rolling green hills"></div>

  <svg class="title-hill" viewBox="0 0 520 170" aria-hidden="true">
    <path d="M0 170 C 60 60, 140 0, 240 6 C 360 12, 400 100, 520 110 L520 170 Z" fill="var(--hill-green)"/>
  </svg>

  <div class="brand-logo"><span class="mark"></span>TotHaven</div>

  <h1 class="page-title"><span>Community</span><span>Connect</span></h1>

  <div class="search">
    <div class="search-field">search</div>
    <span class="search-btn"></span>
  </div>

  <div class="social" aria-label="Social links">
    <span></span><span></span><span></span><span></span><span></span>
  </div>

  <nav class="main-nav">
    <a style="left:34px;width:94px">HOME</a>
    <a style="left:151px;width:139px">ABOUT US</a>
    <a style="left:317px;width:88px">BLOG</a>
    <a style="left:429px;width:186px">TESTIMONIALS</a>
    <a style="left:633px;width:183px">MY ACCOUNT</a>
    <a style="left:834px;width:166px">CONTACT US</a>
  </nav>

  <main class="content-card"></main>

  <div class="art art-boy-waving" role="img" aria-label="Cartoon boy waving over the form"></div>
  <div class="art art-boy-pencil" role="img" aria-label="Cartoon boy riding a flying pencil"></div>

  <h2 class="section-heading">CREATE YOUR ACCOUNT</h2>

  <div class="form-tab">Register</div>
  <div class="form-frame"></div>
  <div class="form-panel"></div>

  <div class="field" style="left:191px;top:471px">Username</div>
  <span class="required-mark" style="left:636px;top:467px">*</span>
  <div class="field" style="left:191px;top:529px">Email Address</div>
  <span class="required-mark" style="left:636px;top:525px">*</span>
  <div class="field" style="left:191px;top:588px">Choose a Password</div>
  <span class="required-mark" style="left:636px;top:584px">*</span>
  <div class="field" style="left:191px;top:647px">Confirm Password</div>
  <span class="required-mark" style="left:636px;top:643px">*</span>

  <div class="field" style="left:669px;top:471px;width:428px;padding-left:22px">Name</div>
  <span class="required-mark" style="left:1108px;top:467px">*</span>
  <p class="privacy-note">this field can be seen by: Anyone</p>

  <p class="required-note">ALL FIELDS WITH *<br>ARE REQUIRED</p>

  <div class="art art-kids-book" role="img" aria-label="Two cartoon kids with pencils standing on an open book"></div>

  <div class="submit-btn">SUBMIT</div>

  <div class="footer-logo">TotHaven</div>
  <p class="copyright">© Copyright 2013 TotHaven. All Rights Reserved</p>
</body>
</html>
```